Broschüre
Zielgruppe
Firmen und Privatpersonen
Unsere Zielkunden sind im bereich Firmen
Firmen die etwas für die Umwelt tun wollen oder sich einen Grünen anstrich geben wollen
Privatpersonen hier ist es die Gruppe die sich für den erhalt der Natur einsetzten die Bienen oder Naturprojekte unterstützen wollen und dergleichen. In der regel Menschen die BIO Kaufen
Aufgabenstellung
Standard Falzflyer DIN-A4 4 Seiten / Logo vorhanden / Unbedingt noch ein Freifeld zum ausfüllen zum bestellen. Daten die wir zum bestellen benötigen Name/Adresse/Telefonnummer/E-Mail/Unterschrift

```html
<!DOCTYPE html>
<html lang="de">
<head>
<meta charset="utf-8">
<title>Bienenpatenschaft – Innenseiten</title>
<link href="https://fonts.googleapis.com/css2?family=Crimson+Text:wght@400;600;700&display=swap" rel="stylesheet">
<style>
  :root{
    --gold:#e1a92f;
    --gold-light:#f3d58a;
    --honey:#c9782a;
    --brown:#6b4810;
    --hex-gold:#d8ad35;
    --hex-brown:#6a4712;
    --ink:#2a2520;
    --paper:#ffffff;
    --backdrop:#c9c9cb;
  }
  html,body{margin:0;width:1200px;height:675px;overflow:hidden;background:var(--backdrop);}
  .spread{
    position:absolute;left:10px;top:42px;width:1863px;height:932px;
    transform:scale(0.6334);transform-origin:0 0;
    background:var(--paper);overflow:hidden;
    font-family:"Crimson Text",Georgia,serif;color:var(--ink);
    box-shadow:0 14px 30px rgba(0,0,0,.25);
  }
  .spread svg.shapes{position:absolute;inset:0;}
  .block{position:absolute;margin:0;font-size:15.6px;line-height:18.8px;}
  .block p{margin:0;}
  .title-vision{position:absolute;left:58px;top:48px;margin:0;font-size:46px;font-weight:700;color:var(--brown);letter-spacing:.5px;}
  .intro{left:56px;top:192px;width:405px;}
  .intro p + p{margin-top:18px;}
  .help{position:absolute;left:123px;top:466px;margin:0;font-size:21px;font-weight:600;border-bottom:1.5px solid var(--ink);line-height:26px;}
  .story{left:492px;top:99px;width:410px;}
  .story .indent{text-indent:22px;}
  .story p + p{margin-top:8px;}
  .steps{position:absolute;left:512px;top:592px;margin:0;padding:0;list-style:none;width:380px;}
  .steps li{position:relative;padding-left:37px;height:56px;font-size:15.6px;line-height:18.8px;}
  .steps li svg{position:absolute;left:0;top:4px;}
  .heading{position:absolute;left:967px;margin:0;font-weight:400;font-size:31px;line-height:36px;}
  .h-engage{top:124px;}
  .h-project{top:411px;}
  .engage{left:967px;top:217px;width:395px;}
  .rule{position:absolute;left:967px;top:381px;width:405px;height:2px;background:var(--ink);}
  .claim{position:absolute;left:967px;top:500px;width:410px;margin:0;font-size:19.5px;line-height:22.5px;}
  .rent{left:967px;top:563px;width:395px;}
  .rent p + p{margin-top:18px;}
  .photo{position:absolute;}
  .photo-comb{left:0;top:247px;width:490px;height:685px;
    background:linear-gradient(90deg,rgba(212,150,50,.85) 0%,rgba(232,186,100,.6) 50%,rgba(255,255,255,0) 100%);}
  .photo-blossom{left:1340px;top:40px;width:523px;height:340px;
    background:radial-gradient(ellipse at 70% 40%,#e9c79a 0%,#f2dcc0 35%,rgba(255,255,255,0) 75%);}
  .photo-honey{left:1350px;top:527px;width:513px;height:380px;
    background:radial-gradient(ellipse at 68% 55%,#c36a1e 0%,#e0a155 35%,#f6dca8 60%,rgba(255,255,255,0) 85%);}
  .photo-bee{left:967px;top:842px;width:140px;height:80px;
    background:radial-gradient(ellipse at 50% 55%,#7a5a2a 0%,#c9a86e 45%,rgba(255,255,255,0) 75%);}
  .cover-white{position:absolute;left:0;top:247px;width:490px;height:250px;
    background:linear-gradient(180deg,rgba(255,255,255,.95) 0%,rgba(255,255,255,.75) 60%,rgba(255,255,255,0) 100%);}
</style>
</head>
<body>
<div class="spread">
  <div class="photo photo-comb" role="img" aria-label="Foto: Bienen auf Honigwaben, nach rechts ausblendend"></div>
  <div class="cover-white"></div>
  <div class="photo photo-blossom" role="img" aria-label="Foto: Biene an einer Borretschblüte"></div>
  <div class="photo photo-honey" role="img" aria-label="Foto: Honiglöffel mit fließendem Honig"></div>
  <div class="photo photo-bee" role="img" aria-label="Foto: einzelne Honigbiene"></div>

  <svg class="shapes" viewBox="0 0 1863 932" width="1863" height="932" aria-hidden="true">
    <path d="M0 0H1863V42C1500 44 900 55 480 100C260 124 90 165 0 200Z" fill="var(--gold)"/>
    <path d="M960 932C1300 918 1620 890 1863 795V932Z" fill="var(--gold)"/>
  </svg>

  <h1 class="title-vision">Die Vision ...</h1>

  <div class="block intro">
    <p>... vom eigenen Honig, vom eigenen Bienenvolk &amp; vom gemeinsamen Bienendorf. Wir lesen es in der Zeitung, wir sehen Berichte im Fernsehen: Das Bienensterben nimmt immer größere Ausmaße an und dies wird, für uns alle, ein elementares Problem werden. Bienen gelten als die wichtigsten bestäubenden Insekten und ihr Fortbestand wird durch weiter zunehmende Wetterkapriolen, abnehmende Lebensräume (Monokulturen), Befall durch Parasiten und vor allem durch den verstärkten Einsatz von Pestiziden in der Landwirtschaft drastisch bedroht.</p>
    <p>Summwiese Burgenland hat sich nun diesem Thema verschrieben. Wir müssen diese Entwicklung bekämpfen. Dies können wir aber nicht allein.</p>
  </div>
  <p class="help">Wir benötigen Ihre HILFE!</p>

  <div class="block story">
    <p class="indent">Daher wird ein nicht unerheblicher Teil aus den Einkünften der Patenschaften dazu verwendet Agrarflächen umzugestalten für alle Bestäubenden Insekten. Flächen werden Gepachtet oder gekauft und umgewidmet das sich die natürlichen Populationen erholen können unter der Schirmherrschaft der Honigbiene. Wir haben im Jahr 2016 / 2017 bereits im Burgenland erste Flächen umgebaut und erste Erfolge erzielt, wie im Umkreis dieser Flächen müssen auch auf konventionellen Flächen weniger Insektizide eingesetzt werden da die natürlichen Feinde dieser Insekten in diesen Habitaten sich vermehrt haben und dies auf natürlichen Wege reguliert haben. Da dies so gut funktioniert haben wir beschlossen dieses Projekt ins Niederösterreich und Oberösterreich zu tragen und suchen daher noch nach unterstützen für dieses Projekt.</p>
    <p class="indent">In Form einer Bienenpatenschaft um 290,00 schenken Sie nicht nur 50.000 fleißigen Bienen (1 Bienenvolk) ein neues Zuhause und ermöglichen diesen die notwendige Pflege, um sicher durch das Jahr zu kommen. (Nahrung, Behandlung gegen Schädlinge, Instandhaltung des Bienenstocks etc.) Sondern ermöglichen auch einen Grundstein für die nächsten Projekte zu setzten.<br>Die Patenschaft bringt Ihnen nicht nur die Gewissheit, Teil eines guten Projekts zu sein. Sie ist natürlich auch fair und funktioniert ganz einfach:</p>
  </div>

  <ul class="steps">
    <li><svg width="30" height="26" viewBox="0 0 30 26"><polygon points="7.5,0 22.5,0 30,13 22.5,26 7.5,26 0,13" fill="var(--hex-gold)"/></svg>Summwiese Burgenland stellt Ihren Bienenstock auf den Feldern des Biohofs auf.</li>
    <li><svg width="30" height="26" viewBox="0 0 30 26"><polygon points="7.5,0 22.5,0 30,13 22.5,26 7.5,26 0,13" fill="var(--hex-brown)"/></svg>Summwiese Burgenland kümmert sich um die Pflege und erntet den Honig.</li>
    <li><svg width="30" height="26" viewBox="0 0 30 26"><polygon points="7.5,0 22.5,0 30,13 22.5,26 7.5,26 0,13" fill="var(--hex-gold)"/></svg>Summwiese Burgenland informiert Sie über Leben und Arbeit Ihrer Bienen.</li>
    <li><svg width="30" height="26" viewBox="0 0 30 26"><polygon points="7.5,0 22.5,0 30,13 22.5,26 7.5,26 0,13" fill="var(--hex-brown)"/></svg>Sie übernehmen die Patenschaft um jährlich 290 Euro pro Bienenstock.</li>
    <li><svg width="30" height="26" viewBox="0 0 30 26"><polygon points="7.5,0 22.5,0 30,13 22.5,26 7.5,26 0,13" fill="var(--hex-gold)"/></svg>Sie können Ihrem Bienenvolk und Ihrer Königin einen Namen geben.</li>
    <li><svg width="30" height="26" viewBox="0 0 30 26"><polygon points="7.5,0 22.5,0 30,13 22.5,26 7.5,26 0,13" fill="var(--hex-brown)"/></svg>Sie bekommen jährlich 6 kg Honig und 2 Flaschen Honigwein Ihres Bienenvolkes.</li>
  </ul>

  <h2 class="heading h-engage">Mit Ihrem<br>Engagement ...</h2>
  <div class="block engage">
    <p>... sichern Sie Tausenden dieser wundervollen Nützlinge das Überleben und ermöglichen eine intensive und nachhaltige Betreuung durch Ihren Imker. Mit einer Bienenpatenschaft können Sie mit Stolz von sich behaupten, einen messbaren Beitrag zum Überleben der Bienen, Erhalt der Nahrungsmittelvielfalt und des Naturschutzes geleistet zu haben.</p>
  </div>
  <div class="rule"></div>

  <h2 class="heading h-project">Projekt Flugsumm<br>Bienenmiete</h2>
  <p class="claim">Werde Imker auf Zeit und miete deinen eigenen Bienenstock voller fleißiger Bestäuber.</p>
  <div class="block rent">
    <p>Wollten Sie schon immer Imker werden und eigenen Honig haben? Jetzt gibt es die Möglichkeit in die Imkerei hinein zu schnuppern und einen Bienenstock für zwei Monate <b>(190 Euro)</b> oder eine Saison <b>(290 Euro)</b> zu „mieten“.</p>
    <p>Nach dieser Zeit gibt es den fix fertig abgefüllten Honig „ihrer“ Bienen in 1-Kilo-Gläsern. „Alles was das Bienenvolk im Honigraum sammelt gehört Ihnen“, und kann an Ihre Liebsten und Freunde verschenkt werden.</p>
  </div>
</div>
</body>
</html>
```